Flyer-Design für IT Support
Zielgruppe
Ich bin spezialisiert auf IT Support für Private Anwender die PC Probleme haben hat bis hin zu kleinen Unternehmen, die keine eigene IT besitzen. Bei kleinen Unternehmen betreue ich das Netzwerk sowie Server.
Aufgabenstellung
Es soll der Support und Verkauf von PCs/Laptops angeboten werden. Mit ansprechenden Texten zum Verkauf von Leistungen und Produkten.

```html
<!DOCTYPE html>
<html lang="de">
<head>
<meta charset="utf-8">
<title>Nordwerk-IT Flyer</title>
<link href="https://fonts.googleapis.com/css2?family=Open+Sans:wght@400;600;700&display=swap" rel="stylesheet">
<style>
:root{
  --blue:#0b69a6;
  --navy:#0a3f66;
  --navy-2:#0e63a0;
  --sky:#e4f2fc;
  --ink:#555b60;
  --label:#a3a7aa;
  --white:#ffffff;
}
*{margin:0;padding:0;box-sizing:border-box}
html,body{width:1200px;height:1029px;overflow:hidden;background:var(--white)}
body{font-family:"Open Sans",Arial,sans-serif;color:var(--ink)}
.canvas{position:relative;width:1200px;height:1029px}

.view-label{position:absolute;font-size:15px;color:var(--label);font-weight:400;text-align:center;width:300px}
.view-rule{position:absolute;height:1px;background:#e2e4e6}

.panel{position:absolute;width:302px;height:432px;overflow:hidden}
.panel svg.bg{position:absolute;left:0;top:0}
.panel-front{left:297px;top:46px}
.panel-back{left:654px;top:48px}

.brand{position:absolute;display:flex;flex-direction:column;align-items:center;color:var(--blue);font-size:14px;font-weight:400;letter-spacing:.2px}
.brand-dot{width:16px;height:16px;border-radius:50%;background:var(--blue);margin-bottom:4px}
.brand-name{border-bottom:1px solid var(--blue);line-height:1.15}

.badge-text{position:absolute;left:140px;top:318px;width:144px;text-align:center;color:var(--blue);font-weight:700;font-size:17px;line-height:19px}
.front-url{position:absolute;left:70px;top:401px;font-size:9px;color:var(--white)}

.help{position:absolute;left:0;width:302px;text-align:center;color:var(--white)}
.help-title{top:126px;font-size:11px;font-weight:700}
.help-body{top:151px;font-size:8.5px;line-height:12px;padding:0 24px}
.help-lead{top:223px;font-size:8.5px;font-weight:700}
.service-list{position:absolute;left:0;top:236px;width:302px;list-style:none;text-align:center;color:var(--white);font-size:8.5px}
.service-list li{height:36px;display:flex;flex-direction:column;align-items:center;justify-content:flex-end}
.service-list li::before{content:"";display:block;border-left:1px dashed rgba(255,255,255,.8);height:22px;margin-bottom:1px}
.service-list li:first-child::before{height:10px;margin-bottom:6px}
.service-list li:first-child{height:24px}
.back-rule{position:absolute;left:20px;top:381px;width:264px;height:1px;background:rgba(255,255,255,.85)}
.contact{position:absolute;left:0;top:392px;width:302px;text-align:center;color:var(--white);font-size:7px;line-height:10.5px}

.spread{position:absolute;left:285px;top:536px;width:609px;height:431px;box-shadow:4px 6px 10px rgba(0,0,0,.18);background:var(--white)}
.strip{position:absolute;height:11px;background:var(--blue)}
.cell{position:absolute;width:305px}
.cell.light{background:var(--white)}
.cell.dark{background:var(--blue)}
.cell-head{position:absolute;left:20px;width:264px;text-align:center;font-weight:700;font-size:11px;padding-bottom:2px;border-bottom:1px solid}
.cell.light .cell-head{color:var(--blue);border-color:var(--blue)}
.cell.dark .cell-head{color:var(--white);border-color:var(--white)}
.service{position:absolute;width:100px;text-align:center;transform:translateX(-50%)}
.service svg{display:block;margin:0 auto}
.service h3{font-size:8.5px;font-weight:700;margin-top:12px;line-height:11px}
.service p{font-size:7.3px;line-height:10.5px}
.service.narrow{width:84px}
.service.narrow h3{white-space:nowrap;margin-left:-8px;margin-right:-8px}
.service.narrow p{font-size:7px}
.cell.light h3{color:var(--blue)}
.cell.light p{color:var(--ink)}
.cell.dark h3,.cell.dark p{color:var(--white)}
.wide{width:124px}
.footnote{position:absolute;left:0;width:305px;top:196px;text-align:center;font-size:5px;color:var(--white)}
</style>
</head>
<body>
<div class="canvas">

  <div class="view-label" style="left:298px;top:20px">geschlossen vorne</div>
  <div class="view-rule" style="left:297px;top:45px;width:302px"></div>
  <div class="view-label" style="left:654px;top:20px">geschlossen hinten</div>
  <div class="view-rule" style="left:654px;top:47px;width:302px"></div>
  <div class="view-label" style="left:442px;top:500px">offen</div>

  <!-- Front cover -->
  <section class="panel panel-front">
    <svg class="bg" width="302" height="432" viewBox="0 0 302 432">
      <defs>
        <linearGradient id="frontBlue" x1="0" y1="0" x2="1" y2="1">
          <stop offset="0" stop-color="#0e6cad"/><stop offset="1" stop-color="#0a4473"/>
        </linearGradient>
        <radialGradient id="photoTone" cx=".5" cy=".45" r=".6">
          <stop offset="0" stop-color="#c9a48a"/><stop offset=".55" stop-color="#b7b3b0"/><stop offset="1" stop-color="#e4f2fc" stop-opacity="0"/>
        </radialGradient>
      </defs>
      <rect width="302" height="432" fill="var(--sky)"/>
      <polygon points="0,0 233,0 0,129" fill="#ffffff"/>
      <line x1="233" y1="0" x2="0" y2="129" stroke="#8e9aa3" stroke-width="2.5"/>
      <g role="img" aria-label="Foto: Mann mit Kapitänsmütze und Ringelshirt zeigt mit beiden Händen das OK-Zeichen">
        <ellipse cx="150" cy="250" rx="150" ry="190" fill="url(#photoTone)"/>
      </g>
      <polygon points="0,400 302,284 302,293 0,408" fill="#ffffff"/>
      <polygon points="0,408 302,293 302,432 0,432" fill="url(#frontBlue)"/>
      <circle cx="212" cy="339" r="72" fill="#ffffff"/>
      <circle cx="212" cy="339" r="65" fill="none" stroke="var(--blue)" stroke-width="2.5"/>
    </svg>
    <div class="brand" style="left:19px;top:20px"><span class="brand-dot"></span><span class="brand-name">Nordwerk-IT</span></div>
    <div class="badge-text">IT BERATUNG<br>IM NORDEN</div>
    <div class="front-url">www.nordwerk-it.de</div>
  </section>

  <!-- Back cover -->
  <section class="panel panel-back">
    <svg class="bg" width="302" height="432" viewBox="0 0 302 432">
      <defs>
        <linearGradient id="backBlue" x1="0" y1="0" x2="1" y2="1">
          <stop offset="0" stop-color="var(--navy)"/><stop offset=".6" stop-color="var(--navy-2)"/><stop offset="1" stop-color="#0b4f82"/>
        </linearGradient>
      </defs>
      <rect width="302" height="432" fill="url(#backBlue)"/>
      <polygon points="72,0 302,0 302,128" fill="#ffffff"/>
    </svg>
    <div class="brand" style="left:198px;top:22px"><span class="brand-dot"></span><span class="brand-name">Nordwerk-IT</span></div>
    <h2 class="help help-title">SIE BRAUCHEN HILFE?</h2>
    <p class="help help-body">Kein Problem... wir sind spezialisiert auf IT Support für Private Anwender die PC Probleme haben bis hin zu kleinen Unternehmen, die keine eigene IT besitzen.<br>Bei kleinen Unternehmen betreue ich das<br>Netzwerk sowie Server.</p>
    <p class="help help-lead">Folgende Dienstleistungen bieten wir an:</p>
    <ul class="service-list">
      <li>Software</li><li>Netzwerk</li><li>Sicherheit</li><li>Hardware</li>
    </ul>
    <div class="back-rule"></div>
    <p class="contact">J. Marlow | IT-Berater | Hafenstraße 8 | 23999 Kirchdorf<br>Telefon: 0176 12345670 | info@nordwerk-it.de | www.nordwerk-it.de</p>
  </section>

  <!-- Open spread -->
  <section class="spread">
    <div class="strip" style="left:0;top:0;width:305px"></div>
    <div class="strip" style="left:304px;top:420px;width:305px"></div>

    <div class="cell light" style="left:0;top:11px;height:206px">
      <h2 class="cell-head" style="top:13px">SOFTWARE</h2>
      <div class="service narrow" style="left:62px;top:36px">
        <svg width="68" height="68" viewBox="0 0 68 68"><circle cx="34" cy="34" r="34" fill="var(--blue)"/><rect x="12" y="24" width="44" height="32" rx="6" fill="#fff"/><path d="M26 24v-5h16v5" fill="none" stroke="#fff" stroke-width="4"/></svg>
        <h3>OFFICE</h3>
        <p>Office Produkte für den Büroalltag sind in der heutigen Zeit nicht mehr wegzudenken.</p>
      </div>
      <div class="service narrow" style="left:152px;top:36px">
        <svg width="68" height="68" viewBox="0 0 68 68"><circle cx="34" cy="34" r="34" fill="var(--blue)"/><g stroke="#fff" stroke-width="4" fill="none"><path d="M26 8v30"/><path d="M44 20v38M44 20h22M44 48h20"/><path d="M22 48v20"/><path d="M4 20h16"/></g><g fill="#fff"><circle cx="26" cy="38" r="5"/><circle cx="40" cy="36" r="5"/><circle cx="22" cy="48" r="5"/><circle cx="40" cy="20" r="5"/></g></svg>
        <h3>VIRTUALISIERUNG</h3>
        <p>Server-Virtualisierung ist heutzutage auch in kleinen Unternehmen einsetzbar. Viele virtuel-le Server sind dabei auf einer physischen Hardware nutzbar.</p>
      </div>
      <div class="service narrow" style="left:242px;top:36px">
        <svg width="68" height="68" viewBox="0 0 68 68"><circle cx="34" cy="34" r="34" fill="var(--blue)"/><rect x="25" y="8" width="18" height="13" fill="#fff"/><path d="M34 21v10M16 31h36M16 31v10M34 31v10M52 31v10" stroke="#fff" stroke-width="2.5" fill="none"/><g fill="none" stroke="#fff" stroke-width="2.5"><rect x="10" y="41" width="12" height="9"/><rect x="28" y="41" width="12" height="9"/><rect x="46" y="41" width="12" height="9"/></g></svg>
        <h3>SERVER</h3>
        <p>Ich installiere und konfiguriere Ihnen Server-Systeme, ange-passt an Ihre Wünsche und Bedürfnisse.</p>
      </div>
    </div>

    <div class="cell dark" style="left:304px;top:11px;height:206px">
      <h2 class="cell-head" style="top:13px">NETZWERK</h2>
      <div class="service wide" style="left:83px;top:36px">
        <svg width="68" height="68" viewBox="0 0 68 68"><circle cx="34" cy="34" r="34" fill="#fff"/><path d="M16 20c10 0 14-3 18-6 4 3 8 6 18 6 0 20-8 30-18 36-10-6-18-16-18-36z" fill="var(--blue)"/></svg>
        <h3>ANTIVIRUS</h3>
        <p>Machen Sie Ihre Daten nicht von Schadsoftware angreifbar, verwenden Sie einen Antiviren Schutz in Ihrer Firma.</p>
      </div>
      <div class="service wide" style="left:225px;top:36px">
        <svg width="68" height="68" viewBox="0 0 68 68"><circle cx="34" cy="34" r="34" fill="#fff"/><path d="M34 10c2 8 14 12 14 26 0 10-6 16-14 16s-14-6-14-16c0-6 3-10 6-12 0 4 2 7 4 8-2-8 2-16 4-22z" fill="var(--blue)"/></svg>
        <h3>FIREWALL</h3>
        <p>Damit Angreifer kein leichtes Spiel haben, an Ihre Firmendaten heranzukommen, verwenden Sie zur Absicherung Ihres Internet-anschlusses eine Firewall.</p>
      </div>
      <p class="footnote">Sicherheit ist wohl eines der wichtigsten Themen in einem Unternehmen.</p>
    </div>

    <div class="cell dark" style="left:0;top:217px;height:203px">
      <h2 class="cell-head" style="top:13px">NETZWERK</h2>
      <div class="service wide" style="left:81px;top:44px">
        <svg width="68" height="68" viewBox="0 0 68 68"><circle cx="34" cy="34" r="34" fill="#fff"/><g fill="none" stroke="var(--blue)" stroke-width="5" stroke-linecap="round"><path d="M12 28a32 32 0 0 1 44 0"/><path d="M19 36a22 22 0 0 1 30 0"/></g><path d="M25 43a13 13 0 0 1 18 0l-9 10z" fill="var(--blue)"/></svg>
        <h3>WLAN</h3>
        <p>WLAN verbindet Ihre Geräte kabellos, allerdings ist es auch wichtig diese abzusichern.</p>
      </div>
      <div class="service wide" style="left:222px;top:44px">
        <svg width="68" height="68" viewBox="0 0 68 68"><circle cx="34" cy="34" r="34" fill="#fff"/><rect x="24" y="10" width="20" height="16" rx="3" fill="var(--blue)"/><path d="M34 26v8M16 34h36M16 34v8M34 34v8M52 34v8" stroke="var(--blue)" stroke-width="3" fill="none"/><g fill="var(--blue)"><rect x="8" y="42" width="16" height="12" rx="3"/><rect x="26" y="42" width="16" height="12" rx="3"/><rect x="44" y="42" width="16" height="12" rx="3"/></g></svg>
        <h3>Netzwerk</h3>
        <p>Um eine schnelle und vor allem sichere Verbindung zu Ihren Geräten herstellen zu können, benötigen Sie eine physikalische Netzwerkverbindung.</p>
      </div>
    </div>

    <div class="cell light" style="left:304px;top:217px;height:203px">
      <h2 class="cell-head" style="top:13px">SOFTWARE</h2>
      <div class="service wide" style="left:82px;top:44px">
        <svg width="68" height="68" viewBox="0 0 68 68"><circle cx="34" cy="34" r="34" fill="var(--blue)"/><rect x="16" y="14" width="34" height="26" rx="6" fill="#fff"/><rect x="22" y="20" width="22" height="14" rx="3" fill="var(--blue)"/><rect x="30" y="40" width="6" height="8" fill="#fff"/><rect x="20" y="48" width="26" height="6" rx="3" fill="#fff"/></svg>
        <h3>CLIENTS</h3>
        <p>Es ist meist effizienter und preis-werter, Hardware für die alltägliche Arbeit selbst zusammenzustellen. Ich berate Sie gerne und konfiguriere den PC für Sie.</p>
      </div>
      <div class="service wide" style="left:222px;top:44px">
        <svg width="68" height="68" viewBox="0 0 68 68"><circle cx="34" cy="34" r="34" fill="var(--blue)"/><circle cx="34" cy="18" r="7" fill="#fff"/><path d="M26 28h16v16h10v10H16V44h10z" fill="#fff"/></svg>
        <h3>ARBEITSPLATZ</h3>
        <p>Ich richte Ihnen Ihre Arbeitsplätze fachgerecht ein; es darf keine Stolpergefahren durch Kabel etc. geben.</p>
      </div>
    </div>
  </section>

</div>
</body>
</html>
```